Commercial Business Card - stand out, clean, simple, unique.

commercial real estate group located in Texas. Called 4 Ridges Real Estate. We want a unique yet clean and professional card. On one side I would like the 4R to be by itself or to look as unique or tasteful as possible. We have the logo in white, black, and color in case a black background or something similar looks best on one side. We need a space for our name, email, cell. website. And possibly room for a phrase or city.

Contact Information for Business Card

Name, Title, Email, Phone Number, website

```html
<!DOCTYPE html>
<html lang="en">
<head>
<meta charset="utf-8">
<title>4 Ridges Real Estate – Business Card</title>
<link rel="stylesheet" href="https://fonts.googleapis.com/css2?family=Cinzel:wght@500&family=PT+Serif&family=Roboto:wght@400&display=swap">
<style>
  :root {
    --backdrop: #c9c9c9;
    --card: #f4f4f4;
    --navy: #1f2a5c;
    --blue: #2a4e9a;
    --ink: #1e1e1e;
    --dark: #1a1a22;
    --red: #b5322a;
    --orange: #d9732a;
  }
  * { box-sizing: border-box; margin: 0; padding: 0; }
  html, body {
    width: 1200px; height: 576px; overflow: hidden;
    background: var(--backdrop);
  }
  .canvas { position: relative; width: 1200px; height: 576px; }
  .card {
    position: absolute; top: 139px;
    width: 484px; height: 290px;
    background: var(--card);
    border-radius: 11px;
    overflow: hidden;
    box-shadow: 0 3px 8px rgba(0,0,0,.22);
  }
  .card--front { left: 82px; }
  .card--back { left: 602px; }

  .stripe {
    position: absolute; left: 0; right: 0; bottom: 0; height: 8px; display: flex;
  }
  .stripe__cool { flex: 1; background: linear-gradient(90deg, var(--blue), var(--dark)); }
  .stripe__warm { flex: 1; background: linear-gradient(90deg, var(--red), var(--orange)); }

  .brand { display: flex; align-items: center; gap: 10px; }
  .brand__dot { width: 14px; height: 14px; border-radius: 50%; background: var(--navy); flex: none; }
  .brand__name {
    font-family: "Cinzel", serif; font-weight: 500; color: var(--navy);
    line-height: 1.05; letter-spacing: .5px;
  }

  .card--front .brand { position: absolute; left: 0; right: 0; top: 108px; justify-content: center; }
  .card--front .brand__name { font-size: 30px; }
  .card--front .brand__dot { width: 22px; height: 22px; }

  .front__web {
    position: absolute; left: 0; right: 0; top: 249px;
    display: flex; align-items: center; justify-content: center; gap: 14px;
    font-family: "Roboto", sans-serif; font-size: 12.5px; color: var(--ink);
  }
  .front__rule { width: 54px; height: 2px; background: linear-gradient(90deg, transparent, var(--orange) 30%, var(--orange) 70%, transparent); }

  .back__tab {
    position: absolute; left: -26px; top: 34px;
    width: 36px; height: 72px; border-radius: 0 36px 36px 0; background: var(--blue);
  }
  .person { position: absolute; left: 28px; top: 48px; }
  .person__name { font-family: "PT Serif", serif; font-size: 20px; color: var(--ink); }
  .person__title { font-family: "Roboto", sans-serif; font-size: 12px; color: var(--ink); margin-top: 3px; }

  .card--back .brand { position: absolute; right: 30px; top: 52px; gap: 8px; }
  .card--back .brand__name { font-size: 19px; text-align: left; }
  .card--back .brand__dot { width: 12px; height: 12px; }

  .contacts {
    position: absolute; left: 28px; top: 204px; list-style: none;
    font-family: "Roboto", sans-serif; font-size: 12.5px; color: var(--ink);
  }
  .contacts li { display: flex; align-items: center; gap: 12px; height: 18.5px; }
  .contacts svg { width: 11px; height: 11px; fill: var(--orange); flex: none; }

  .address {
    position: absolute; right: 29px; top: 218px; text-align: right;
    font-family: "Roboto", sans-serif; font-size: 12.5px; line-height: 21px; color: var(--ink);
  }
</style>
</head>
<body>
<main class="canvas">
  <section class="card card--front">
    <div class="brand">
      <span class="brand__dot"></span>
      <span class="brand__name">4 Ridges<br>Real Estate</span>
    </div>
    <div class="front__web">
      <span class="front__rule"></span>
      <span>www.4ridgesrealestate.com</span>
      <span class="front__rule"></span>
    </div>
    <div class="stripe"><span class="stripe__cool"></span><span class="stripe__warm"></span></div>
  </section>

  <section class="card card--back">
    <span class="back__tab"></span>
    <div class="person">
      <p class="person__name">Daniel Reyes Hart</p>
      <p class="person__title">Managing Director</p>
    </div>
    <div class="brand">
      <span class="brand__dot"></span>
      <span class="brand__name">4 Ridges<br>Real Estate</span>
    </div>
    <ul class="contacts">
      <li>
        <svg viewBox="0 0 12 12" aria-hidden="true"><path d="M1 4c0-1.5 2-2.5 5-2.5S11 2.5 11 4v1H8.5V3.8h-5V5H1zM3 6h6l1.5 5h-9z"/></svg>
        <span>5550-214-7788</span>
      </li>
      <li>
        <svg viewBox="0 0 12 12" aria-hidden="true"><path d="M0 2h12v8H0zM1 3l5 4 5-4v-.2H1z" fill-rule="evenodd"/></svg>
        <span>dhart@4ridgesrealestate.com</span>
      </li>
      <li>
        <svg viewBox="0 0 12 12" aria-hidden="true"><path d="M6 .5a5.5 5.5 0 1 0 0 11 5.5 5.5 0 0 0 0-11zm0 1.2c.7.8 1.2 2.2 1.3 3.7H4.7C4.8 3.9 5.3 2.5 6 1.7zM1.7 6.6h2c.1 1.4.5 2.6 1 3.4A4.3 4.3 0 0 1 1.7 6.6zm0-1.2a4.3 4.3 0 0 1 3-3.4c-.5.8-.9 2-1 3.4zm3 1.2h2.6c-.1 1.5-.6 2.9-1.3 3.7-.7-.8-1.2-2.2-1.3-3.7zm3.6 0h2a4.3 4.3 0 0 1-3 3.4c.5-.8.9-2 1-3.4zm0-1.2c-.1-1.4-.5-2.6-1-3.4a4.3 4.3 0 0 1 3 3.4z"/></svg>
        <span>www.4ridgesrealestate.com</span>
      </li>
    </ul>
    <address class="address" style="font-style:normal">118, Mesa Ridge Rd,<br>Austin, TX 78701</address>
    <div class="stripe"><span class="stripe__cool"></span><span class="stripe__warm"></span></div>
  </section>
</main>
</body>
</html>
```